Acupuncture Medspa needs a business card design

I need a business card design that looks professional, has a spa-like quality and can offer a promo on the back. Initial promo is "First session free". The tagline of NeedleNook is: Refresh, Restore, Rejuvenate.

NeedleNook is a membership-based acupuncture medspa that offers acupuncture, cupping, and herbal therapies. Members choose between the "Refresh" membership which is for stress relief, or "Restore" which is for treating health conditions, and lastly "Rejuvenate" which is for natural facial enhancement.

Industry/Entity Type

Health And Wellness

Contact Information for Business Card

Coral Haskins, MAC, L.Ac.
612-555-0193
www.needlenook-example.com

Font styles to use
Serif
Sans Serif

Colors

Designer to choose colors to be used in the design.

Requirements
Must have
• The project must have NeedleNook logo, promo on the back, and contact information
Nice to have
• I would like to see the colors of the logo used.

```html
<!DOCTYPE html>
<html lang="en">
<head>
<meta charset="utf-8">
<title>NeedleNook Business Card</title>
<link href="https://fonts.googleapis.com/css2?family=Montserrat:wght@400;500;600&display=swap" rel="stylesheet">
<style>
  :root {
    --teal: #14877f;
    --ink: #3a3a3a;
    --muted: #6a6a6a;
    --brown: #3a2418;
    --paper: #ffffff;
    --stage: #9a9a9a;
  }
  * { box-sizing: border-box; margin: 0; padding: 0; }
  html, body { width: 1200px; height: 930px; overflow: hidden; }
  body {
    background: var(--stage);
    font-family: "Montserrat", sans-serif;
    position: relative;
  }
  .card {
    position: absolute;
    left: 250px;
    width: 700px;
    height: 400px;
    border-radius: 30px;
    overflow: hidden;
  }
  .card-front { top: 45px; background: var(--teal); }
  .card-back { top: 485px; background: var(--paper); }

  .wordmark {
    display: flex;
    align-items: center;
    gap: 14px;
    font-weight: 500;
    letter-spacing: 2px;
    text-transform: uppercase;
  }
  .wordmark .dot {
    border-radius: 50%;
    border: 3px solid currentColor;
  }
  .front-lockup {
    position: absolute;
    left: 50%; top: 50%;
    transform: translate(-50%, -50%);
    display: flex;
    flex-direction: column;
    align-items: center;
    gap: 18px;
    color: var(--paper);
  }
  .card-front .wordmark { font-size: 50px; }
  .card-front .wordmark .dot { width: 56px; height: 56px; }
  .tagline {
    font-size: 17px;
    letter-spacing: 3px;
    font-weight: 400;
  }

  .card-back .wordmark {
    position: absolute;
    left: 48px; top: 58px;
    color: var(--teal);
    font-size: 34px;
  }
  .card-back .wordmark .dot { width: 40px; height: 40px; }

  .person {
    position: absolute;
    right: 44px; top: 108px;
    text-align: right;
  }
  .person-name {
    color: var(--teal);
    font-weight: 600;
    font-size: 26px;
    letter-spacing: 0.5px;
  }
  .person-role { color: var(--ink); font-size: 15px; margin-top: 2px; }

  .divider {
    position: absolute;
    left: 120px; right: 44px; top: 192px;
    height: 2px;
    background: var(--teal);
  }
  .address {
    position: absolute;
    right: 44px; top: 208px;
    text-align: right;
    color: var(--ink);
    font-size: 15px;
    line-height: 1.45;
  }
  .contacts {
    position: absolute;
    left: 48px; top: 240px;
    list-style: none;
    color: var(--ink);
    font-size: 18px;
    line-height: 1.55;
  }
  .contacts li { display: flex; align-items: center; gap: 10px; }
  .contacts svg { width: 14px; height: 14px; fill: none; stroke: var(--teal); stroke-width: 2; flex: none; }
  .contacts .accent { color: var(--teal); font-weight: 500; }

  .footer-band { position: absolute; left: 0; bottom: 0; width: 700px; height: 80px; }
  .promo {
    position: absolute;
    right: 0; bottom: 0;
    width: 218px; height: 72px;
    display: flex;
    align-items: center;
    justify-content: center;
    padding-left: 12px;
    color: var(--paper);
    font-size: 15px;
    font-weight: 600;
    letter-spacing: 0.5px;
  }
</style>
</head>
<body>
  <section class="card card-front">
    <div class="front-lockup">
      <div class="wordmark"><span class="dot"></span>NeedleNook</div>
      <p class="tagline">Refresh, Restore, Rejuvenate</p>
    </div>
  </section>

  <section class="card card-back">
    <div class="wordmark"><span class="dot"></span>NeedleNook</div>

    <div class="person">
      <div class="person-name">CORAL HASKINS</div>
      <div class="person-role">MAC, L.Ac. · Director</div>
    </div>

    <div class="divider"></div>

    <div class="address">48 Willow Bend<br>Road Easton, FL 33010</div>

    <ul class="contacts">
      <li><svg viewBox="0 0 14 14"><path d="M3 1 L5 4 L4 6 Q6 9 8 10 L10 9 L13 11 L11 13 Q4 12 1 3 Z"/></svg><span>612-555-0193</span></li>
      <li><svg viewBox="0 0 14 14"><rect x="1" y="3" width="12" height="8"/><path d="M1 3 L7 8 L13 3"/></svg><span>info@needlenook-example.com</span></li>
      <li><svg viewBox="0 0 14 14"><circle cx="7" cy="7" r="6"/><path d="M1 7 H13 M7 1 Q3 7 7 13 M7 1 Q11 7 7 13"/></svg><span>www.<span class="accent">needlenook-example</span>.com</span></li>
    </ul>

    <svg class="footer-band" viewBox="0 0 700 80" preserveAspectRatio="none" aria-hidden="true">
      <rect x="0" y="66" width="455" height="14" fill="var(--brown)"/>
      <polygon points="470,80 482,8 700,8 700,80" fill="var(--teal)"/>
    </svg>
    <p class="promo">First session free</p>
  </section>
</body>
</html>
```